Business / Stationery Design Project

Hi,

I need business cards and all other stationary designed for my new finance broking business.

Stationary required:

Business card
Letter head
with compliments
envelopes

There is gold in the logo design so some gold would be good and open to other creative ideas / colours.

Regards
Tomas
Updates

Project Deadline Extended
Reason: Still working through designs.

Target Market(s)

Small to medium business customers. Also to appeal to referrers who include accounting firms and other associated professionals (valuers etc)

Industry/Entity Type

Finance

Requirements
Must have
• Professional, classy look.

```html
<!DOCTYPE html>
<html lang="en">
<head>
<meta charset="utf-8">
<title>Harlow Finance – DL Envelope</title>
<link rel="stylesheet" href="https://fonts.googleapis.com/css2?family=Arimo:wght@400;700&display=swap">
<style>
  :root {
    --backdrop: #4b3f2b;
    --paper: #f4f4f2;
    --gold: #c8a25a;
    --charcoal: #1f1f21;
    --ink: #2a2a2c;
    --ink-soft: #4a4a4d;
  }
  * { margin: 0; padding: 0; box-sizing: border-box; }
  html, body {
    width: 1200px;
    height: 720px;
    overflow: hidden;
    background: var(--backdrop);
  }
  .canvas {
    position: relative;
    width: 1200px;
    height: 720px;
    display: flex;
    align-items: center;
    justify-content: center;
  }
  .envelope {
    position: relative;
    width: 1000px;
    height: 500px;
    background: var(--paper);
    box-shadow: 0 10px 30px rgba(0,0,0,0.35);
  }
  .envelope__band {
    position: absolute;
    top: 0;
    left: 0;
    width: 100%;
    height: 16px;
    display: flex;
  }
  .envelope__band-gold { width: 48%; background: var(--gold); }
  .envelope__band-dark { flex: 1; background: var(--charcoal); }
  .sender {
    position: absolute;
    top: 44px;
    left: 40px;
    font-family: "Arimo", Arial, sans-serif;
  }
  .brand {
    display: flex;
    align-items: center;
    gap: 10px;
  }
  .brand__dot {
    width: 16px;
    height: 16px;
    border-radius: 50%;
    background: var(--gold);
  }
  .brand__name {
    font-weight: 700;
    font-size: 24px;
    letter-spacing: 1px;
    color: var(--ink);
    text-transform: uppercase;
  }
  .sender__address {
    margin-top: 30px;
    font-style: normal;
    font-weight: 400;
    font-size: 13px;
    line-height: 1.3;
    color: var(--ink-soft);
  }
</style>
</head>
<body>
  <main class="canvas">
    <section class="envelope" aria-label="DL envelope">
      <div class="envelope__band">
        <span class="envelope__band-gold"></span>
        <span class="envelope__band-dark"></span>
      </div>
      <div class="sender">
        <div class="brand">
          <span class="brand__dot"></span>
          <span class="brand__name">Harlow Finance</span>
        </div>
        <address class="sender__address">
          Harlow Finance PTY LTD<br>
          ABN: 42 318 604 275<br>
          U3 / 14 Wattle Rd<br>
          Kellyville, NSW 2155<br>
          Australia
        </address>
      </div>
    </section>
  </main>
</body>
</html>
```